Letterhead for Business Law Firm

We need a letter head for our firm based on the design we have settled on and it is attached. Our clients are small and large businesses around the world, and our letterhead is used typically for formal legal purposes such as demand letters (accusing the recipient of doing bad things) or responding to demand letters. It may also be sent to regulators and other government agencies. So this needs to be tasteful, but a little edgy as well - we try to convey that we are a firm that is different - businesses and investors come to us for creative, quick advice, typically in high stress circumstances, and for our ability to work through high conflict situations, and rapid paced engagements.

Target Market(s)

Lawyers, business executives, investors, government regulators who may receive letters from this firm on behalf of its clients.

Industry/Entity Type

Business

Requirements
Must have
• The design and the firm's contact information:
• Thornvale Law Firm, P.C.
• 8172 SW 17th Ave
• Portland, OR 97058
• phone: 971 555 0147
• fax: 971 555 0182
• in what placement and how depicted (e.g. a phone icon instead of the word "phone") I leave to your creative ideas.
Nice to have
• design and information can be placed at the top, bottom and/or sides of the letter, and the design should be for a standard letter size paper - and can have a separate design for the second page.

```html
<!DOCTYPE html>
<html lang="en">
<head>
<meta charset="utf-8">
<title>Thornvale Law Firm, P.C. — Letterhead</title>
<link rel="stylesheet" href="https://fonts.googleapis.com/css2?family=Barlow:wght@400;500&display=swap">
<style>
  :root {
    --paper: #ffffff;
    --edge: #9a9a9a;
    --ink: #2b2b2b;
    --ink-soft: #444444;
    --band-dark: #151515;
    --band-teal: #3f6b6c;
    --band-text: #ffffff;
    --icon-glyph: #3a3a3a;
  }
  * { margin: 0; padding: 0; box-sizing: border-box; }
  html, body {
    width: 845px;
    height: 1200px;
    overflow: hidden;
    background: var(--paper);
  }
  .letterhead {
    position: relative;
    width: 845px;
    height: 1200px;
    background: var(--paper);
    border: 1px solid var(--edge);
    font-family: "Barlow", sans-serif;
    color: var(--ink);
  }
  .brand {
    position: absolute;
    top: 34px;
    left: 0;
    width: 100%;
    text-align: center;
    font-weight: 400;
    font-size: 36px;
    letter-spacing: 12px;
    padding-left: 12px;
    line-height: 1;
    color: var(--ink);
  }
  .address {
    position: absolute;
    top: 1139px;
    left: 0;
    width: 100%;
    text-align: center;
    font-size: 13.5px;
    font-weight: 500;
    letter-spacing: 0.2px;
    line-height: 16px;
    color: var(--ink-soft);
    white-space: nowrap;
  }
  .contact-band {
    position: absolute;
    left: 0;
    bottom: 1px;
    width: 100%;
    height: 40px;
    background: linear-gradient(90deg,
      var(--band-dark) 0%,
      #3a3f40 12%,
      var(--band-teal) 45%,
      var(--band-teal) 60%,
      #3a4546 88%,
      var(--band-dark) 100%);
  }
  .contact-item {
    position: absolute;
    top: 11px;
    display: flex;
    align-items: center;
    gap: 8px;
    font-size: 12.5px;
    font-weight: 500;
    line-height: 17px;
    color: var(--band-text);
    letter-spacing: 0.2px;
    white-space: nowrap;
  }
  .contact-item svg { width: 17px; height: 17px; flex: none; }
  .contact-phone { left: 118px; }
  .contact-email { left: 375px; }
  .contact-web { left: 601px; }
</style>
</head>
<body>
  <div class="letterhead">
    <div class="brand">THORNVALE</div>

    <p class="address">Thornvale Law Firm, P.C. &nbsp;·&nbsp; 8172 SW 17th Ave, Portland, OR 97058</p>

    <div class="contact-band">
      <div class="contact-item contact-phone">
        <svg viewBox="0 0 20 20" aria-hidden="true">
          <circle cx="10" cy="10" r="9.5" fill="var(--band-text)"/>
          <path d="M7 5.5c.6-.3 1.1 0 1.4.6l.7 1.6c.2.5 0 .9-.4 1.2l-.6.4c.5 1.3 1.4 2.3 2.6 2.9l.5-.6c.3-.4.8-.5 1.2-.3l1.5.8c.5.3.7.9.4 1.4-.6 1-1.7 1.4-2.8 1-2.7-1-4.6-3-5.5-5.7-.3-1.2.1-2.8 1-3.3z" fill="var(--icon-glyph)"/>
        </svg>
        <span>971 555 0147 &nbsp;|&nbsp; Fax 971 555 0182</span>
      </div>
      <div class="contact-item contact-email">
        <svg viewBox="0 0 20 20" aria-hidden="true">
          <circle cx="10" cy="10" r="9.5" fill="var(--band-text)"/>
          <rect x="5" y="6.5" width="10" height="7" rx="0.8" fill="var(--icon-glyph)"/>
          <path d="M5.4 7l4.6 3.6L14.6 7" fill="none" stroke="var(--band-text)" stroke-width="0.9"/>
        </svg>
        <span>info@thornvale.com</span>
      </div>
      <div class="contact-item contact-web">
        <svg viewBox="0 0 20 20" aria-hidden="true">
          <circle cx="10" cy="10" r="9.5" fill="var(--band-text)"/>
          <g fill="none" stroke="var(--icon-glyph)" stroke-width="1">
            <circle cx="10" cy="10" r="5.5"/>
            <ellipse cx="10" cy="10" rx="2.4" ry="5.5"/>
            <line x1="4.5" y1="10" x2="15.5" y2="10"/>
            <line x1="5.3" y1="7.3" x2="14.7" y2="7.3"/>
            <line x1="5.3" y1="12.7" x2="14.7" y2="12.7"/>
          </g>
        </svg>
        <span>www.thornvale.com</span>
      </div>
    </div>
  </div>
</body>
</html>
```